MODELS AGENCY NEW YEAR 2026 CARD

A 10 cm x 21 cm horizontal New Year card for clients of our 2 models agencies, Pommelin (kids) and Velvaride (actors and adults) (logo in the jobs).

Side A of the card: creative mission:
-text: 2026
-text: Peace and Love
-Studio or movie set atmosphere
-tone of voice: optimistic, positive, colorful

Side B:
(name of 4 people of the agency:)
Odette, Anne-Sophie, Hortense & Luc-Antoine,
(2 logos)
Pommelin & VelvaRide
(Adres)
Rue des Tilleuls 74 b3 - 1200 Bruxelles - Belgique

Target Market(s)

Movie directors, photographers

Industry/Entity Type

Fashion, advertising & Movies

Requirements
Must have
• SEE TEXT IN BRIEFING

```html
<!DOCTYPE html>
<html lang="fr">
<head>
<meta charset="utf-8">
<title>Pommelin &amp; VelvaRide – New Year Card 2026</title>
<link rel="stylesheet" href="https://fonts.googleapis.com/css2?family=Bebas+Neue&family=Montserrat:wght@500;700&family=Roboto:wght@400;700&display=swap">
<style>
  :root {
    --page: #ffffff;
    --agency-blue: #009ade;
    --ink-white: #ffffff;
    --brand-purple: #3b1f5c;
    --brand-orange: #e8501c;
    --night-top: #2a1540;
    --night-mid: #6a2a3a;
    --glow-bottom: #d9661c;
  }
  * { margin: 0; padding: 0; box-sizing: border-box; }
  html, body { width: 1200px; height: 1200px; overflow: hidden; background: var(--page); }
  .canvas { position: relative; width: 1200px; height: 1200px; }

  .card { position: absolute; left: 10px; top: 319px; width: 1180px; height: 562px; display: flex; }

  /* Side B */
  .side-contact {
    width: 590px; height: 100%; background: var(--agency-blue); position: relative;
    color: var(--ink-white); font-family: "Roboto", Arial, sans-serif; text-align: center;
  }
  .team-names { position: absolute; top: 56px; left: 0; width: 590px; font-weight: 700; font-size: 30px; line-height: 39px; }
  .brand-panel {
    position: absolute; left: 51px; top: 175px; width: 485px; height: 183px;
    background: var(--ink-white); border-radius: 9px; display: flex;
  }
  .brand { flex: 1; display: flex; flex-direction: column; align-items: center; justify-content: center; gap: 8px; }
  .brand-name { font-family: "Montserrat", Arial, sans-serif; font-weight: 700; font-size: 34px; line-height: 1; display: flex; align-items: center; gap: 8px; }
  .brand-name .dot { width: 12px; height: 12px; border-radius: 50%; display: inline-block; }
  .brand--kids .brand-name { color: var(--brand-purple); }
  .brand--kids .dot { background: var(--agency-blue); }
  .brand--adults .brand-name { color: var(--brand-purple); }
  .brand--adults .dot { background: var(--brand-orange); }
  .brand-line { font-size: 10px; letter-spacing: 1.2px; color: var(--brand-purple); text-transform: uppercase; }
  .brand-since { font-size: 8px; color: var(--brand-purple); margin-top: 14px; }

  .divider { position: absolute; left: 76px; top: 404px; }
  .address { position: absolute; top: 460px; left: 0; width: 590px; font-size: 25px; line-height: 34px; font-weight: 400; }

  /* Side A */
  .side-mission { width: 590px; height: 100%; position: relative; overflow: hidden; color: var(--ink-white); text-align: center; }
  .scene-backdrop {
    position: absolute; inset: 0;
    background:
      radial-gradient(circle at 75% 72%, rgba(232,110,40,.55), transparent 55%),
      linear-gradient(180deg, var(--night-top) 0%, var(--night-mid) 40%, var(--glow-bottom) 100%);
  }
  .mission-title {
    position: absolute; left: 0; width: 100%; top: 122px;
    font-family: "Bebas Neue", "Arial Narrow", sans-serif; font-size: 100px; line-height: 82px;
    padding-left: 130px; padding-right: 0; text-align: center; width: 560px;
  }
  .mission-year {
    position: absolute; left: 150px; width: 300px; top: 318px;
    font-family: "Montserrat", Arial, sans-serif; font-weight: 500; font-size: 118px; line-height: 1; letter-spacing: -4px;
  }
  .mission-motto {
    position: absolute; left: 136px; width: 320px; top: 496px;
    font-family: "Roboto", Arial, sans-serif; font-weight: 700; font-size: 34px; line-height: 1; white-space: nowrap;
  }
</style>
</head>
<body>
<div class="canvas">
  <div class="card">
    <section class="side-contact">
      <p class="team-names">Odette, Anne-Sophie<br>Hortense &amp; Luc-Antoine</p>

      <div class="brand-panel">
        <div class="brand brand--kids">
          <span class="brand-name"><span class="dot"></span>Pommelin</span>
          <span class="brand-line">Children models agency</span>
          <span class="brand-since">– SINCE 1982 –</span>
        </div>
        <div class="brand brand--adults">
          <span class="brand-name"><span class="dot"></span>VelvaRide</span>
          <span class="brand-line">People, actors &amp; models agency</span>
          <span class="brand-since">– SINCE 2000 –</span>
        </div>
      </div>

      <svg class="divider" width="444" height="40" viewBox="0 0 444 40" aria-hidden="true">
        <g stroke="#ffffff" stroke-opacity=".7" stroke-width="1">
          <line x1="10" y1="18" x2="206" y2="18"/><line x1="10" y1="22" x2="206" y2="22"/>
          <line x1="252" y1="18" x2="448" y2="18"/><line x1="252" y1="22" x2="448" y2="22"/>
        </g>
        <path d="M230 38 C222 28 215 22 215 14 a15 15 0 0 1 30 0 C245 22 238 28 230 38 Z" fill="#ffffff"/>
        <circle cx="230" cy="14" r="5.5" fill="#009ade"/>
      </svg>

      <p class="address">Rue des Tilleuls 74 b3 - 1200<br>Bruxelles - Belgique</p>
    </section>

    <section class="side-mission">
      <div class="scene-backdrop" role="img" aria-label="Night city skyline with fireworks and a glowing studio clock in warm orange light"></div>
      <h1 class="mission-title">CREATIVE<br>MISSION</h1>
      <p class="mission-year">2026</p>
      <p class="mission-motto">PEACE AND LOVE</p>
    </section>
  </div>
</div>
</body>
</html>
```